Stonefield General Contracting Business Card

My company is a General Contracting and Handyman service based in a private community in Northeast Pennsylvania.
Our cliental is a mix of year round and seasonal homeowners
We pride ourselves i using new and innovative building techniques and always try to build with pride and integrity
Please check my website f(under construction) or a list of services and more information
The files below are my logo and my facebook business page profile pic

Industry/Entity Type

Building

Contact Information for Business Card

Stonefield General Contracting
Dale Hurtig
Alder Ridge, Pennsylvania
570-314-2796
dale@stnfldco.com
www.stnfldco.com
www.pagenook.example/stonefieldcontracting

```html
<!DOCTYPE html>
<html lang="en">
<head>
<meta charset="utf-8">
<title>Stonefield General Contracting – Business Card</title>
<link rel="stylesheet" href="https://fonts.googleapis.com/css2?family=Arimo:wght@700&family=Lato:wght@400;500&display=swap">
<style>
  :root {
    --card-black: #0a0a0a;
    --brand-red: #e3130f;
    --licence-red: #b5151b;
    --band-dark: #1a0306;
    --text-white: #ffffff;
    --name-grey: #e6e6e6;
  }
  html, body {
    margin: 0;
    padding: 0;
    overflow: hidden;
    background: var(--card-black);
  }
  .card {
    position: relative;
    width: 1200px;
    height: 722px;
    background: var(--card-black);
    overflow: hidden;
    font-family: "Lato", Arial, sans-serif;
    color: var(--text-white);
  }
  .brand-mark {
    position: absolute;
    left: 160px;
    top: 130px;
    width: 190px;
    height: 190px;
    background: var(--brand-red);
  }
  .company-name {
    position: absolute;
    left: 441px;
    top: 178px;
    margin: 0;
    font-family: "Arimo", Arial, sans-serif;
    font-weight: 700;
    color: var(--text-white);
    line-height: 1;
  }
  .company-name .primary {
    display: block;
    font-size: 80px;
    letter-spacing: 1px;
  }
  .company-name .secondary {
    display: block;
    margin-top: 10px;
    font-size: 57px;
    letter-spacing: 0.5px;
  }
  .name-band {
    position: absolute;
    left: 0;
    top: 371px;
    width: 1200px;
    height: 87px;
    background: linear-gradient(to bottom,
      var(--brand-red) 0%,
      #a00a0c 12%,
      var(--band-dark) 45%,
      var(--band-dark) 60%,
      #7a0709 85%,
      var(--brand-red) 100%);
    display: flex;
    align-items: center;
    justify-content: center;
  }
  .person-name {
    margin: 0 0 0 40px;
    font-size: 43px;
    font-weight: 500;
    color: var(--name-grey);
    letter-spacing: 0.5px;
    line-height: 1;
  }
  .location {
    position: absolute;
    left: 86px;
    top: 511px;
    display: flex;
    align-items: center;
    gap: 16px;
    margin: 0;
    font-size: 33px;
    line-height: 40px;
  }
  .social-link {
    position: absolute;
    left: 86px;
    top: 574px;
    margin: 0;
    font-size: 26px;
    line-height: 32px;
  }
  .social-link .accent { color: var(--brand-red); }
  .licence {
    position: absolute;
    left: 86px;
    top: 616px;
    margin: 0;
    font-size: 31px;
    line-height: 38px;
    color: var(--licence-red);
    letter-spacing: 0.5px;
  }
  .contact-right {
    position: absolute;
    left: 712px;
    top: 506px;
    margin: 0;
    padding: 0;
    list-style: none;
  }
  .contact-right li {
    display: flex;
    align-items: center;
    gap: 16px;
    height: 44px;
    font-size: 35px;
  }
  .icon { flex: none; fill: var(--brand-red); }
</style>
</head>
<body>
<div class="card">
  <div class="brand-mark" aria-hidden="true"></div>

  <h1 class="company-name">
    <span class="primary">Stonefield</span>
    <span class="secondary">General Contracting</span>
  </h1>

  <div class="name-band">
    <p class="person-name">Dale Hurtig</p>
  </div>

  <p class="location">
    <svg class="icon" width="30" height="26" viewBox="0 0 28 24" aria-hidden="true">
      <path d="M14 1 L1 12 L4 12 L4 23 L11 23 L11 16 L17 16 L17 23 L24 23 L24 12 L27 12 Z"/>
    </svg>
    Alder Ridge, Pennsylvania
  </p>
  <p class="social-link">www.<span class="accent">pagenook</span>.example/<span class="accent">stonefield</span>contracting</p>
  <p class="licence">PA HIC - 048213</p>

  <ul class="contact-right">
    <li>
      <svg class="icon" width="26" height="22" viewBox="0 0 26 22" aria-hidden="true">
        <path d="M2 7 C2 2 24 2 24 7 L24 9 L18 9 L18 6 L8 6 L8 9 L2 9 Z"/>
        <path d="M6 10 L20 10 L24 21 L2 21 Z"/>
        <circle cx="13" cy="15" r="3" fill="#0a0a0a"/>
      </svg>
      570-314-2796
    </li>
    <li>
      <svg class="icon" width="26" height="20" viewBox="0 0 26 20" aria-hidden="true">
        <path d="M1 2 L25 2 L25 18 L1 18 Z M3 4 L13 12 L23 4" stroke="#0a0a0a" stroke-width="1.5"/>
      </svg>
      dale@stnfldco.com
    </li>
    <li>
      <svg class="icon" width="26" height="26" viewBox="0 0 26 26" aria-hidden="true">
        <circle cx="13" cy="13" r="11" fill="none" stroke="#e3130f" stroke-width="2.5"/>
        <ellipse cx="13" cy="13" rx="5" ry="11" fill="none" stroke="#e3130f" stroke-width="2"/>
        <path d="M2 13 H24 M4 7 H22 M4 19 H22" stroke="#e3130f" stroke-width="2"/>
      </svg>
      www.stnfldco.com
    </li>
  </ul>
</div>
</body>
</html>
```